plumfable business card

need to upgrade current business card for an online retailer of handmade arts and crafts, please visit plumfable.com.au

need to be artistic professional look

sample layout, contents, logo, are in the attached files

need for 4 people, details for other 2 people to be provided later

```html
<!DOCTYPE html>
<html lang="en">
<head>
<meta charset="utf-8">
<title>Plumfable Business Card</title>
<link href="https://fonts.googleapis.com/css2?family=Lato:wght@300;400;700;900&display=swap" rel="stylesheet">
<style>
  :root {
    --page-bg: #e4e4e4;
    --card-black: #121212;
    --brand-red: #c8161b;
    --brand-red-deep: #8e0c10;
    --divider-grey: #3a3a3a;
    --logo-grey: #545454;
    --white: #ffffff;
    --ink: #111111;
  }
  html, body {
    margin: 0;
    padding: 0;
    width: 1200px;
    height: 926px;
    overflow: hidden;
    background: var(--page-bg);
    font-family: "Lato", sans-serif;
  }
  .sheet {
    position: relative;
    width: 1200px;
    height: 926px;
  }
  .card {
    position: absolute;
    left: 240px;
    width: 720px;
    height: 411px;
    box-shadow: 0 8px 22px rgba(0,0,0,0.25);
  }
  .card--front { top: 38px; }
  .card--back  { top: 477px; }
  .card svg { display: block; width: 720px; height: 411px; }

  .fill-black { fill: var(--card-black); }
  .fill-red { fill: url(#redTexture); }
  .fill-red-flat { fill: var(--brand-red); }
  .fill-white { fill: var(--white); }
  .fill-divider { fill: var(--divider-grey); }

  .brand-name { font: 700 60px "Lato", sans-serif; fill: var(--logo-grey); letter-spacing: 1px; }
  .person-first { font-weight: 300; }
  .person-last { font-weight: 900; }
  .person-name { font-size: 34px; fill: var(--white); font-family: "Lato", sans-serif; }
  .person-title { font: 700 15px "Lato", sans-serif; fill: var(--white); }
  .contact-line { font: 400 19px "Lato", sans-serif; fill: var(--white); }
  .contact-label { font-weight: 900; }

  .back-intro { font: 400 15px "Lato", sans-serif; fill: var(--white); letter-spacing: 0.5px; }
  .back-headline { font: 400 22px "Lato", sans-serif; fill: var(--white); letter-spacing: 0.5px; }
  .offer-item { font: 400 15px "Lato", sans-serif; fill: var(--white); }
  .bullet { fill: var(--brand-red); }
  .encourage-title { font: 900 24px "Lato", sans-serif; fill: var(--ink); letter-spacing: 0.5px; }
  .encourage-text { font: 400 17px "Lato", sans-serif; fill: var(--white); letter-spacing: 0.5px; }
</style>
</head>
<body>
<main class="sheet">

  <section class="card card--front" aria-label="Business card front">
    <svg viewBox="0 0 720 411" xmlns="http://www.w3.org/2000/svg">
      <defs>
        <radialGradient id="redTexture" cx="55%" cy="40%" r="75%">
          <stop offset="0%" stop-color="#cf1a1f"/>
          <stop offset="70%" stop-color="#a91216"/>
          <stop offset="100%" stop-color="#7f0a0d"/>
        </radialGradient>
        <pattern id="hatch" width="5" height="7" patternUnits="userSpaceOnUse" patternTransform="skewX(-30)">
          <rect width="2" height="7" fill="#e9a0a2"/>
        </pattern>
      </defs>
      <rect class="fill-black" width="720" height="411"/>
      <polygon class="fill-red-flat" points="0,150 40,190 0,230"/>
      <rect class="fill-divider" x="250" y="0" width="12" height="411"/>
      <rect class="fill-red" x="262" y="0" width="458" height="411"/>
      <polygon class="fill-divider" points="264,150 196,205 264,260"/>
      <polygon class="fill-white" points="262,166 216,205 262,244"/>
      <rect class="fill-white" x="248" y="0" width="16" height="24"/>
      <rect class="fill-white" x="248" y="387" width="16" height="24"/>

      <text class="brand-name" x="130" y="205" text-anchor="middle" transform="rotate(-90 130 205)" dy="20">Plumfable</text>

      <text class="person-name" x="300" y="152"><tspan class="person-first">KIRAN </tspan><tspan class="person-last">THAPA</tspan></text>
      <text class="person-title" x="300" y="178">Director, Plumfable Australia</text>
      <rect x="300" y="188" width="238" height="7" fill="url(#hatch)"/>
      <text class="contact-line" x="300" y="248"><tspan class="contact-label">E.</tspan> kiran@plumfable.com.au</text>
      <text class="contact-line" x="300" y="276"><tspan class="contact-label">P.</tspan> +61 400 555 019</text>
    </svg>
  </section>

  <section class="card card--back" aria-label="Business card back">
    <svg viewBox="0 0 720 411" xmlns="http://www.w3.org/2000/svg">
      <defs>
        <linearGradient id="bandRed" x1="0" y1="0" x2="1" y2="1">
          <stop offset="0%" stop-color="#b81418"/>
          <stop offset="50%" stop-color="#d41c21"/>
          <stop offset="100%" stop-color="#a51115"/>
        </linearGradient>
      </defs>
      <rect class="fill-black" width="720" height="411"/>
      <polygon class="fill-red-flat" points="326,0 394,0 360,40"/>

      <rect x="0" y="230" width="720" height="181" fill="url(#bandRed)"/>
      <polygon class="fill-black" points="314,228 406,228 360,272"/>
      <polygon points="330,230 390,230 360,258" fill="#c0171c"/>
      <rect class="fill-white" x="0" y="222" width="28" height="10"/>
      <rect class="fill-white" x="692" y="222" width="28" height="10"/>
      <rect class="fill-white" x="0" y="399" width="28" height="12"/>
      <rect class="fill-white" x="692" y="399" width="28" height="12"/>

      <text class="back-intro" x="360" y="78" text-anchor="middle">VISIT US FOR EXOTIC HAND MADE</text>
      <text class="back-headline" x="360" y="106" text-anchor="middle">ART &amp; CRAFTS ARROUND THE GLOBE</text>

      <circle class="bullet" cx="156" cy="140" r="4"/>
      <text class="offer-item" x="166" y="145">Thai Traditional Paintings</text>
      <text class="offer-item" x="166" y="171">Lokta / Rice Paper Crats</text>
      <circle class="bullet" cx="402" cy="154" r="4"/>
      <text class="offer-item" x="412" y="159">Nepali / Tibeten Thangkas</text>
      <text class="offer-item" x="412" y="185">Allo/Cotton/Woollen Itemes</text>

      <text class="encourage-title" x="360" y="310" text-anchor="middle">WE ENCOURAGE</text>
      <text class="encourage-text" x="360" y="340" text-anchor="middle">ECO-FRIENDLY, SUSTAINABLE AND TRADITIONAL ARTS PRACTICE</text>
    </svg>
  </section>

</main>
</body>
</html>
```